TB - WESITE NEEDED PAGE: Clean / Modern / Pro & Dynamic

Tavlin-Brokers is a new insurance brokerage firm dealing exclusively with companies (BToB) providing the following property: Liabilities Insurance Insurances Automobile Insurance Insurances Construction% 26amp; Engineering Casualty Workmen 's Compensation Health Insurance Marime% 26amp; Transit Credit Insurance Young, Fast, Proactive and Dynamic we call ourselves Tavlin-Brokers because we are a "start-up" willing to make a difference in the market, bringing modernity and speed to our industry, still too bureaucratic / procedural / opaque uninitiated. We need something respecting the colors of our orange logtype; blue; white; black; easy to scroll, with simple information on the company; - who we are - our team (with the pictures) - what we do - what we do - contact us, contact us (google map) Luanda (Angola) Small company, just need something flashy / professional / structured / modern.

Target Market(s)

BtoB; Oil and gas companies; French speaking copying established in Angola, all industrials, factories and importers of goods.

Industry/Entity Type

Insurance Broker

Font styles to use
Sans Serif

Colors

Designer to choose colors to be used in the design.

Requirements
Must have
• We need something respecting the colors of our orange logtype; blue; white; black; easy to scroll, with simple information on the company; - who we are - our team (with the pictures) - what we do - what we do - contact us, contact us (google map) Luanda (Angola) Small company, just need something flashy / professional / structured / modern.
Nice to have
• A page format
Should not have
• WE DO NOT WANT A REFER TO OUR LOGO, but a Home Page for our Website with the basics categories ... >> PLEASE CAREFULLY USE THE RIGHT COLOR OF THE LOGOTYPE which are the ones enclosed Orange / Turquoise / Black as per the business card .

```html
<!DOCTYPE html>
<html lang="en">
<head>
<meta charset="utf-8">
<title>Tavlin-Brokers | Insurance Brokerage</title>
<link href="https://fonts.googleapis.com/css2?family=Montserrat:wght@800&family=Open+Sans:ital,wght@0,400;0,600;0,700;1,700&display=swap" rel="stylesheet">
<style>
:root{
  --teal:#1cb0c2;
  --teal-light:#a8e3ea;
  --orange:#f2891f;
  --ink:#111;
  --text:#333;
  --muted:#555;
  --band:#e1e6ea;
  --white:#fff;
  --footer:#0c0c0c;
}
*{box-sizing:border-box;margin:0;padding:0}
html,body{width:1200px;height:3958px;overflow:hidden;background:var(--white)}
body{font-family:"Open Sans",Arial,sans-serif;color:var(--text)}
.page{position:relative;width:1200px;height:3958px;overflow:hidden}
.abs{position:absolute}

/* top bar */
.topbar{left:223px;top:0;width:752px;height:25px;background:var(--teal);clip-path:polygon(0 0,100% 0,97.5% 100%,2.5% 100%)}
.topbar-item{position:absolute;top:5px;color:var(--white);font-size:11px;display:flex;align-items:center;gap:6px}
.social-sq{position:absolute;top:4px;width:17px;height:17px;background:var(--ink)}
/* nav */
.brand-nav{left:220px;top:42px;color:var(--orange);font-weight:700;font-size:9px;letter-spacing:.2px;display:flex;align-items:center;gap:6px}
.brand-dot{width:22px;height:22px;border-radius:50%;border:3px solid var(--orange)}
.menu{top:48px;font-size:10.5px;font-weight:600;color:var(--ink);letter-spacing:.3px}
.search-btn{left:831px;top:43px;width:31px;height:25px;background:var(--orange);display:flex;align-items:center;justify-content:center}
.quote-btn{left:875px;top:43px;width:103px;height:25px;background:var(--ink);border:2px solid var(--orange);color:var(--orange);font-size:10.5px;display:flex;align-items:center;justify-content:center;letter-spacing:.3px}
.nav-rule{left:0;top:80px;width:1200px;height:3px;background:var(--orange)}

/* hero */
.hero-bg{left:0;top:83px;width:1200px;height:620px;background:linear-gradient(90deg,#dfe7f1 0%,#eef2f8 40%,#f4f6fa 70%,#eaeff6 100%)}
.hero-photo{left:0;top:83px;width:620px;height:600px;background:radial-gradient(ellipse at 45% 45%,#d9b39a 0%,#c99a80 35%,#b3c3d6 70%,rgba(223,231,241,0) 100%)}
.hero-mark{left:815px;top:172px;width:100px;height:100px;border-radius:50%;border:5px solid var(--orange)}
.hero-title{left:600px;top:287px;width:530px;text-align:center;font-family:"Montserrat",sans-serif;font-weight:800;font-size:40px;color:var(--ink);letter-spacing:1px}
.hero-rule{left:732px;top:353px;width:162px;height:4px;background:linear-gradient(90deg,var(--teal) 0 50%,var(--orange) 50% 100%)}
.hero-text{left:622px;top:381px;width:495px;font-size:16.6px;line-height:29.5px;color:var(--text);text-align:justify}
.btn{position:absolute;height:33px;color:var(--white);font-size:15px;display:flex;align-items:center;padding-left:16px}
.btn .sep{position:absolute;right:40px;top:7px;width:1px;height:19px;background:rgba(255,255,255,.7)}
.btn .go{position:absolute;right:12px;top:10px;width:13px;height:13px;border-radius:50%;border:2px solid var(--white)}
.btn-orange{background:var(--orange)}
.btn-teal{background:var(--teal)}
.hero-curve{left:0;top:560px;width:1200px;height:150px}

/* section titles */
.sec-mark{width:46px;height:46px;border-radius:50%;border:3px solid var(--orange);left:577px}
.sec-title{left:0;width:1200px;text-align:center;color:var(--teal);font-weight:600;font-size:28px}
.sec-rule{left:566px;width:68px;height:3px;background:var(--orange)}
.sec-lead{left:220px;width:760px;text-align:center;font-size:10.6px;line-height:22px;color:var(--text)}

/* who we are */
.who-frame{left:233px;top:903px;width:317px;height:438px;background:var(--teal)}
.who-photo{left:223px;top:917px;width:318px;height:438px;background:linear-gradient(160deg,#c9d3dd 0%,#8f9aa7 40%,#2b2f37 75%,#15171b 100%)}
.feature{position:absolute;top:952px;width:140px;text-align:center}
.feature svg{display:block;margin:0 auto}
.feature-label{margin-top:8px;font-weight:700;font-style:italic;font-size:18px;line-height:19px;color:var(--ink)}
.who-text{left:593px;top:1096px;width:388px;font-size:10.2px;line-height:26.5px;text-align:justify;color:var(--muted)}

/* what we do */
.wwd-band{left:0;top:1383px;width:1200px;height:945px;clip-path:polygon(0 7.7%,100% 0,100% 92%,0 100%);background-color:var(--band);background-image:radial-gradient(rgba(255,255,255,.45) 1px,transparent 1px);background-size:5px 5px}
.card{position:absolute;width:368px;height:220px;background:var(--white);border-top:3px solid var(--teal);box-shadow:0 2px 6px rgba(0,0,0,.12)}
.card.active{background:var(--teal)}
.card-img{position:absolute;left:20px;top:-27px;width:149px;height:216px}
.card-body{position:absolute;left:189px;top:0;width:162px}
.card-icon{position:absolute;top:32px}
.card-title{position:absolute;top:68px;font-weight:700;font-size:14.5px;letter-spacing:1.5px;line-height:23px;color:var(--teal)}
.card-copy{position:absolute;top:117px;width:162px;font-size:10.4px;line-height:17px;text-align:justify;color:var(--text)}
.card-more{position:absolute;top:175px;font-weight:700;font-size:11.5px;color:var(--orange)}
.card.active .card-title,.card.active .card-copy,.card.active .card-more{color:var(--white)}
.card.active .card-more{text-decoration:underline}

/* team */
.member{position:absolute;top:2542px;width:231px;height:315px}
.member-photo{position:absolute;left:0;top:0;width:231px;height:279px;border:2px solid var(--teal);background:var(--white)}
.member-photo .fig{position:absolute;left:25px;top:25px;width:181px;height:252px}
.member-name{position:absolute;top:284px;width:231px;text-align:center;font-size:14px;color:var(--teal)}
.member-role{position:absolute;top:302px;width:231px;text-align:center;font-size:10.5px;font-style:italic;color:var(--teal)}
.member.active .member-photo{background:#b8b9bb;border-color:#b8b9bb}
.member.active .band{position:absolute;left:0;top:279px;width:231px;height:40px;background:var(--teal)}
.member.active .member-name,.member.active .member-role{color:var(--white)}
.team-social{position:absolute;left:45px;top:248px;display:flex;gap:8px}
.team-social span{width:24px;height:24px;border-radius:50%;border:1.5px solid var(--white)}
.team-social span.on{background:var(--teal)}
.divider{left:0;top:2923px;width:1200px;height:1px;background:var(--teal)}

/* contact form */
.field{position:absolute;border:1.5px solid #aab0ba;background:var(--white);font-size:11px;color:var(--text);padding:12px 10px}
.submit{left:616px;top:3193px;width:364px;height:39px;background:var(--orange);color:var(--white);font-weight:700;font-size:18px;display:flex;align-items:center;justify-content:center;letter-spacing:.5px}

/* contact band */
.contact-band{left:0;top:3272px;width:1200px;height:100px;background:var(--teal)}
.contact-item{position:absolute;top:3292px;width:200px;text-align:center;color:var(--white);font-size:16px}
.contact-item .ic{width:36px;height:36px;border-radius:50%;background:var(--white);margin:0 auto 8px;display:flex;align-items:center;justify-content:center}
.contact-sep{top:3285px;width:1px;height:77px;background:rgba(255,255,255,.75)}
.map{left:0;top:3372px;width:1200px;height:281px;background:linear-gradient(120deg,#ececec 0%,#e5ebe1 35%,#c9def0 55%,#e9ece7 75%,#ececec 100%)}
.map-card{left:558px;top:3459px;width:195px;height:82px;background:var(--white);box-shadow:0 1px 5px rgba(0,0,0,.25);text-align:center}
.map-card h4{margin-top:22px;font-weight:400;font-size:15px;color:var(--teal)}
.map-card p{font-size:10px;color:var(--text);margin-top:3px}

/* footer */
.footer{left:0;top:3653px;width:1200px;height:273px;background:var(--footer)}
.foot-mark{left:294px;top:3690px;width:80px;height:80px;border-radius:50%;border:5px solid var(--orange)}
.foot-brand{left:223px;top:3765px;font-weight:700;font-size:24px;color:var(--orange);letter-spacing:.5px}
.foot-text{left:223px;top:3806px;width:240px;font-size:10px;line-height:16px;color:var(--white)}
.foot-social{position:absolute;top:3868px;width:22px;height:22px;border:1.5px solid var(--white)}
.foot-head{top:3724px;font-weight:700;font-size:14px;color:var(--white)}
.foot-list{list-style:none;font-size:10.8px;color:var(--white)}
.foot-list li{height:25px;display:flex;align-items:center;gap:8px}
.foot-list li::before{content:"";width:12px;height:1.5px;background:var(--teal)}
.foot-list li.current{color:var(--teal)}
.copyright{left:0;top:3926px;width:1200px;height:32px;text-align:center;font-size:10px;line-height:32px;color:var(--text)}
</style>
</head>
<body>
<div class="page">

  <!-- Top bar -->
  <div class="abs topbar"></div>
  <div class="topbar-item" style="left:272px">
    <svg width="12" height="12" viewBox="0 0 12 12"><path d="M6 1a3.5 3.5 0 0 0-3.5 3.5C2.5 7.5 6 11 6 11s3.5-3.5 3.5-6.5A3.5 3.5 0 0 0 6 1z" fill="#fff"/><circle cx="6" cy="4.5" r="1.3" fill="#1cb0c2"/></svg>Address</div>
  <div class="topbar-item" style="left:356px">
    <svg width="12" height="12" viewBox="0 0 12 12"><path d="M3 1l2 2.5-1.2 1.3a7 7 0 0 0 3.4 3.4L8.5 7 11 9l-1.5 2C5 10.5 1.5 7 1 2.5z" fill="#fff"/></svg>Phone</div>
  <div class="topbar-item" style="left:436px">
    <svg width="18" height="12" viewBox="0 0 18 12"><rect x="0" y="0" width="18" height="12" fill="#fff"/><path d="M0 0l9 7 9-7" fill="none" stroke="#1cb0c2" stroke-width="1.5"/></svg>E-Mail</div>
  <div class="social-sq" style="left:891px"></div>
  <div class="social-sq" style="left:916px"></div>
  <div class="social-sq" style="left:941px"></div>

  <!-- Navigation -->
  <div class="abs brand-nav"><span class="brand-dot"></span>TAVLIN-BROKERS</div>
  <div class="abs menu" style="left:379px">HOME</div>
  <div class="abs menu" style="left:431px">WHO WE ARE</div>
  <div class="abs menu" style="left:518px">WHAT WE DO</div>
  <div class="abs menu" style="left:604px">CONTACT US</div>
  <div class="abs search-btn"><svg width="14" height="14" viewBox="0 0 14 14"><circle cx="6" cy="6" r="4.3" fill="none" stroke="#fff" stroke-width="1.8"/><path d="M9.2 9.2L13 13" stroke="#fff" stroke-width="2"/></svg></div>
  <div class="abs quote-btn">GET A QUOTE</div>
  <div class="abs nav-rule"></div>

  <!-- Hero -->
  <div class="abs hero-bg"></div>
  <div class="abs hero-photo" role="img" aria-label="Smiling family of four posing close together"></div>
  <div class="abs hero-mark"></div>
  <h1 class="abs hero-title">INSURING YOUR TRUST</h1>
  <div class="abs hero-rule"></div>
  <p class="abs hero-text">Lorem ipsum dolor sit amet, consectetur adipiscing elit, sed do eiusmod tempor incididunt ut labore et dolore magna aliqua. Ut enim ad minim veniam, quis nostrud exercitation</p>
  <div class="btn btn-orange" style="left:705px;top:499px;width:151px">Contact Us<span class="sep"></span><span class="go"></span></div>
  <div class="btn btn-teal" style="left:874px;top:499px;width:152px">View More<span class="sep"></span><span class="go"></span></div>
  <svg class="abs hero-curve" viewBox="0 0 1200 150" preserveAspectRatio="none">
    <path d="M0 30 C250 170 700 140 1200 30 L1200 150 L0 150 Z" fill="#a8e3ea"/>
    <path d="M0 30 C250 140 700 130 1200 30" fill="none" stroke="#f2891f" stroke-width="3"/>
    <path d="M80 70 C300 150 700 150 1200 36 C700 160 300 165 80 70 Z" fill="#1cb0c2"/>
    <path d="M0 60 C280 190 700 170 1200 40 L1200 150 L0 150 Z" fill="#fff"/>
  </svg>

  <!-- Who We Are -->
  <div class="abs sec-mark" style="top:771px"></div>
  <h2 class="abs sec-title" style="top:822px">Who We Are</h2>
  <div class="abs sec-rule" style="top:866px"></div>
  <div class="abs who-frame"></div>
  <div class="abs who-photo" role="img" aria-label="Three business people in suits standing together in an office"></div>

  <div class="feature" style="left:577px">
    <svg width="76" height="70" viewBox="0 0 76 70"><polygon points="19,2 57,2 74,35 57,68 19,68 2,35" fill="#fff" stroke="#f2891f" stroke-width="3"/><rect x="25" y="38" width="5" height="12" fill="#f2891f"/><rect x="33" y="32" width="5" height="18" fill="#f2891f"/><rect x="41" y="35" width="5" height="15" fill="#f2891f"/><rect x="49" y="26" width="5" height="24" fill="#f2891f"/><path d="M24 32l10-8 8 4 12-10" fill="none" stroke="#f2891f" stroke-width="2"/></svg>
    <div class="feature-label">Experience</div>
  </div>
  <div class="feature" style="left:729px">
    <svg width="76" height="70" viewBox="0 0 76 70"><polygon points="19,2 57,2 74,35 57,68 19,68 2,35" fill="#fff" stroke="#f2891f" stroke-width="3"/><circle cx="30" cy="27" r="5" fill="#f2891f"/><circle cx="46" cy="27" r="5" fill="#f2891f"/><circle cx="38" cy="33" r="6" fill="#f2891f"/><path d="M22 46a8 8 0 0 1 16 0zM38 46a8 8 0 0 1 16 0z" fill="#f2891f"/><path d="M28 50a10 9 0 0 1 20 0z" fill="#f2891f"/></svg>
    <div class="feature-label">Well Trained<br>Experts</div>
  </div>
  <div class="feature" style="left:866px">
    <svg width="76" height="70" viewBox="0 0 76 70"><polygon points="19,2 57,2 74,35 57,68 19,68 2,35" fill="#fff" stroke="#f2891f" stroke-width="3"/><circle cx="38" cy="35" r="15" fill="none" stroke="#f2891f" stroke-width="6"/><circle cx="38" cy="35" r="15" fill="none" stroke="#fff" stroke-width="6" stroke-dasharray="5 18.5"/></svg>
    <div class="feature-label">Flexible<br>Benefits</div>
  </div>
  <p class="abs who-text">Sed ut perspiciatis unde omnis iste natus error sit voluptatem accusantium doloremque laudantium, totam rem aperiam, eaque ipsa quae ab illo inventore veritatis et quasi architecto beatae vitae dicta sunt explicabo. Nemo enim ipsam voluptatem quia voluptas sit aspernatur aut odit aut fugit, sed quia consequuntur magni dolores eos qui ratione voluptatem sequi nesciunt. Neque porro quisquam est, qui dolorem ipsum quia dolor sit amet, consectetur, adipisci velit, sed quia non numquam</p>
  <div class="btn btn-orange" style="left:829px;top:1287px;width:152px">Read More<span class="sep"></span><span class="go"></span></div>

  <!-- What We Do -->
  <div class="abs wwd-band"></div>
  <div class="abs sec-mark" style="top:1475px"></div>
  <h2 class="abs sec-title" style="top:1528px">What We Do</h2>
  <div class="abs sec-rule" style="top:1572px"></div>
  <p class="abs sec-lead" style="top:1595px">Lorem ipsum dolor sit amet, consectetur adipiscing elit, sed do eiusmod tempor incididunt ut labore et dolore magna aliqua. Ut enim ad minim veniam, quis nostrud exercitation ullamco laboris nisi ut aliquip ex ea commodo consequat.</p>

  <div class="card" style="left:223px;top:1694px">
    <div class="card-img" role="img" aria-label="Hand signing an insurance contract with a pen" style="background:linear-gradient(150deg,#eef1f5 0%,#d9dee5 55%,#c6b7a8 100%)"></div>
    <div class="card-body">
      <svg class="card-icon" width="40" height="38" viewBox="0 0 40 38"><path d="M8 6l10 4v10c0 8-10 14-10 14S-2 28-2 20V10z" transform="translate(4 0)" fill="#f2891f"/><circle cx="28" cy="6" r="4" fill="#f2891f"/><rect x="23" y="12" width="10" height="22" rx="2" fill="#f2891f"/></svg>
      <div class="card-title">LIABILITIES<br>INSURANCE</div>
      <p class="card-copy">Lorem ipsum dolor sit amet, consectetur adipiscing elit, sed do eiusmod tempor incididunt.</p>
      <div class="card-more">READ MORE</div>
    </div>
  </div>
  <div class="card active" style="left:612px;top:1694px">
    <div class="card-img" role="img" aria-label="Smiling man sitting at the wheel of a car" style="background:linear-gradient(150deg,#c2c6cc 0%,#7d828a 50%,#2e3136 100%)"></div>
    <div class="card-body">
      <svg class="card-icon" width="42" height="34" viewBox="0 0 42 34"><path d="M8 4h26l6 12v14h-7v-4H9v4H2V16z" fill="#fff"/><path d="M11 8h20l3 7H8z" fill="#1cb0c2"/><circle cx="10" cy="20" r="3" fill="#1cb0c2"/><circle cx="32" cy="20" r="3" fill="#1cb0c2"/></svg>
      <div class="card-title">AUTOMOBILE<br>INSURANCE</div>
      <p class="card-copy">Lorem ipsum dolor sit amet, consectetur adipiscing elit, sed do eiusmod tempor incididunt.</p>
      <div class="card-more">READ MORE &#10230;</div>
    </div>
  </div>
  <div class="card" style="left:223px;top:1980px">
    <div class="card-img" role="img" aria-label="Family with a child visiting a doctor in a clinic" style="background:linear-gradient(150deg,#e9ecef 0%,#c6cbd0 50%,#6b5a50 100%)"></div>
    <div class="card-body">
      <svg class="card-icon" width="42" height="38" viewBox="0 0 42 38"><path d="M21 16S12 10 12 5a4.5 4.5 0 0 1 9-1 4.5 4.5 0 0 1 9 1c0 5-9 11-9 11z" fill="#f2891f"/><path d="M2 26l8-5h10l6 3h-9 9l8-5 4 2-12 10H10l-8-1z" fill="#f2891f"/></svg>
      <div class="card-title">HEALTH<br>INSURANCE</div>
      <p class="card-copy">Lorem ipsum dolor sit amet, consectetur adipiscing elit, sed do eiusmod tempor incididunt.</p>
      <div class="card-more">READ MORE</div>
    </div>
  </div>
  <div class="card" style="left:612px;top:1980px">
    <div class="card-img" role="img" aria-label="Two colleagues reviewing a tablet beside a computer" style="background:linear-gradient(150deg,#eceff2 0%,#bfc4ca 50%,#4a4e55 100%)"></div>
    <div class="card-body">
      <svg class="card-icon" width="48" height="36" viewBox="0 0 48 36"><rect x="0" y="0" width="48" height="36" rx="4" fill="#f2891f"/><rect x="0" y="8" width="48" height="4" fill="#fff"/><rect x="9" y="19" width="9" height="7" fill="none" stroke="#fff" stroke-width="2"/><rect x="24" y="19" width="15" height="2.5" fill="#fff"/><rect x="24" y="24" width="10" height="2.5" fill="#fff"/></svg>
      <div class="card-title">CREDIT<br>INSURANCE</div>
      <p class="card-copy">Lorem ipsum dolor sit amet, consectetur adipiscing elit, sed do eiusmod tempor incididunt.</p>
      <div class="card-more">READ MORE</div>
    </div>
  </div>

  <!-- Our Team -->
  <div class="abs sec-mark" style="top:2350px"></div>
  <h2 class="abs sec-title" style="top:2406px">Our Team</h2>
  <div class="abs sec-rule" style="top:2451px"></div>
  <p class="abs sec-lead" style="top:2474px">Lorem ipsum dolor sit amet, consectetur adipiscing elit, sed do eiusmod tempor incididunt ut labore et dolore magna aliqua. Ut enim ad minim veniam, quis nostrud exercitation ullamco laboris nisi ut aliquip ex ea commodo consequat.</p>

  <div class="member" style="left:220px">
    <div class="member-photo"><div class="fig" role="img" aria-label="Team member in a blue shirt with arms crossed" style="background:linear-gradient(180deg,#fff 0%,#b9cde6 45%,#6f93c4 100%)"></div></div>
    <div class="member-name">Name</div>
    <div class="member-role">Designation</div>
  </div>
  <div class="member active" style="left:484px">
    <div class="member-photo"><div class="fig" role="img" aria-label="Senior team member in a dark suit" style="background:linear-gradient(180deg,#b8b9bb 0%,#7c7e82 40%,#25272b 100%)"></div>
      <div class="team-social"><span></span><span></span><span class="on"></span><span></span></div>
    </div>
    <div class="band"></div>
    <div class="member-name">Name</div>
    <div class="member-role">Designation</div>
  </div>
  <div class="member" style="left:750px">
    <div class="member-photo"><div class="fig" role="img" aria-label="Team member in glasses and a black suit" style="background:linear-gradient(180deg,#fff 0%,#c6c8cc 40%,#1d1f23 100%)"></div></div>
    <div class="member-name">Name</div>
    <div class="member-role">Designation</div>
  </div>
  <div class="abs divider"></div>

  <!-- Get In Touch -->
  <div class="abs sec-mark" style="top:2957px"></div>
  <h2 class="abs sec-title" style="top:3011px">Get In Touch</h2>
  <div class="abs sec-rule" style="top:3055px"></div>
  <div class="field" style="left:221px;top:3083px;width:369px;height:37px">Name</div>
  <div class="field" style="left:613px;top:3083px;width:367px;height:37px">E-Mail</div>
  <div class="field" style="left:221px;top:3140px;width:369px;height:100px;padding-top:9px">Message</div>
  <div class="field" style="left:613px;top:3140px;width:367px;height:37px">Phone</div>
  <div class="abs submit">SUBMIT</div>

  <!-- Contact band -->
  <div class="abs contact-band"></div>
  <div class="contact-item" style="left:152px">
    <div class="ic"><svg width="16" height="18" viewBox="0 0 16 18"><path d="M8 1a6 6 0 0 0-6 6c0 5 6 10 6 10s6-5 6-10a6 6 0 0 0-6-6z" fill="#1cb0c2"/><circle cx="8" cy="7" r="2.2" fill="#fff"/></svg></div>Address</div>
  <div class="abs contact-sep" style="left:430px"></div>
  <div class="contact-item" style="left:502px">
    <div class="ic"><svg width="18" height="13" viewBox="0 0 18 13"><rect width="18" height="13" rx="2" fill="#1cb0c2"/><path d="M1 1l8 6 8-6" fill="none" stroke="#fff" stroke-width="1.6"/></svg></div>Mail</div>
  <div class="abs contact-sep" style="left:783px"></div>
  <div class="contact-item" style="left:857px">
    <div class="ic"><svg width="16" height="16" viewBox="0 0 12 12"><path d="M3 1l2 2.5-1.2 1.3a7 7 0 0 0 3.4 3.4L8.5 7 11 9l-1.5 2C5 10.5 1.5 7 1 2.5z" fill="#1cb0c2"/></svg></div>Phone</div>

  <!-- Map -->
  <div class="abs map" role="img" aria-label="Street map of the office location in Luanda with a park and lake"></div>
  <svg class="abs" style="left:542px;top:3384px" width="30" height="44" viewBox="0 0 30 44"><path d="M15 1A13 13 0 0 0 2 14c0 11 13 28 13 28s13-17 13-28A13 13 0 0 0 15 1z" fill="#e53935"/><circle cx="15" cy="14" r="4.5" fill="#a31515"/></svg>
  <div class="abs map-card"><h4>ADDRESS</h4><p>Lorem ipsum dolor sit ame</p></div>

  <!-- Footer -->
  <div class="abs footer"></div>
  <div class="abs foot-mark"></div>
  <div class="abs foot-brand">TAVLIN-BROKERS</div>
  <p class="abs foot-text">Lorem ipsum dolor sit amet, consectetur adipiscing elit, sed do eiusmod tempor incididunt ut labore et dolore magna aliqua.</p>
  <div class="foot-social" style="left:226px"></div>
  <div class="foot-social" style="left:256px"></div>
  <div class="foot-social" style="left:286px"></div>
  <div class="foot-social" style="left:316px"></div>

  <div class="abs foot-head" style="left:587px">QUICK LINKS</div>
  <ul class="abs foot-list" style="left:587px;top:3765px">
    <li class="current">HOME</li><li>Who We Are</li><li>What We Do</li><li>Contact Us</li>
  </ul>
  <div class="abs foot-head" style="left:823px">EXTRA LINKS</div>
  <ul class="abs foot-list" style="left:823px;top:3765px">
    <li>LIABILITIES INSURANCE</li><li>AUTOMOBILE INSURANCE</li><li>HEALTH INSURANCE</li><li>CREDIT INSURANCE</li>
  </ul>
  <div class="abs copyright">&copy; 2019 TAVLIN BROKERS. All Rights Reserved</div>
</div>
</body>
</html>
```